Zielgruppe
Unsere Firma produziert individuelles Büromaterialen aus Papier & Kunststoff (bspw. Ringbücher, Klarsichthüllen, Mappen, etc.) Zielgruppe sind (eher konservative) Unternehmenskunden in allen Branchen (speziell Logistik, KFZ, Gesundheit).
Die Broschüre soll primär zur Neukundenakquise als auch für Neuverkäufe an Bestandskunden verwendet werden und in einem schlichten, modernen und hochwertigen Design eine Übersicht über unser Produktportfolio bieten.
Aufgabenstellung
Die Broschüre soll auf Basis des bestehenden Corporate Designs gestaltet werden.
1) In der Broschüre soll jede unserer fünf Produktkategorien (Ordner, Ringbuchordner, Ordnerregister, Hüllen & Taschen, Mappen) eine eigene Seite/Abschnitt erhalten, ähnlich unserer Website.
2) Zudem soll auf einer eigenen Seite/Abschnitt prägnant darauf hingewiesen werden, dass wir für alle Produktkategorie individuelle Sonderanfertigungen anbieten.
Die Strukturierung und Aufteilung der Inhalt in der Broschüre soll sich relativ klar an unserer Website orientieren. Medien & bereits vorhandene Texte sind sowohl als Anlage dem Projekt beigefügt, als auch auf unserer Website auffindbar. Falls notwendig wären wir auch bereit zu einzelnen Themenbereiche neue Texte erstellen zu lassen.
Hinsichtlich des Formats überlassen wir die Auswahl dem Designer. Die Broschüre wird jedoch auch häufig in digitaler Form versandt.

```html
<!DOCTYPE html>
<html lang="de">
<head>
<meta charset="utf-8">
<title>Norvel Plastik – Produktbroschüre</title>
<link rel="stylesheet" href="https://fonts.googleapis.com/css2?family=Arimo:wght@400;700&family=Open+Sans:wght@300;400;600;700&family=Source+Sans+3:wght@400;600;700&display=swap">
<style>
:root{
  --page:#151515;
  --page-deep:#0f0f0f;
  --ink:#e9e9e9;
  --muted:#bdbdbd;
  --blue:#4a8fd6;
  --green:#1aa55a;
  --navy:#2c3547;
  --slate:#3f5873;
  --gold:#d9cf2a;
  --rule:#3d5a80;
}
*{box-sizing:border-box;margin:0;padding:0}
html,body{width:1200px;height:960px;overflow:hidden;background:#fff}
body{position:relative;font-family:"Source Sans 3",sans-serif;color:var(--ink)}
.spread{position:absolute;background:var(--page);overflow:hidden}
.abs{position:absolute}
.body{font-size:6.3px;line-height:1.38}
.body p{margin-bottom:4px}
.bold{font-weight:700}
.kicker{font-family:"Open Sans",sans-serif;font-weight:300;letter-spacing:.06em}
.head-blue{font-family:"Open Sans",sans-serif;font-weight:700;color:var(--blue)}
.head-green{font-family:"Open Sans",sans-serif;font-weight:400;color:var(--green);letter-spacing:.05em}
ul.bullets{list-style:disc;padding-left:12px}
.callout{border-left:1.5px solid var(--rule);padding-left:6px;font-weight:700}
.photo{position:absolute;border-radius:50%}
.arimo{font-family:"Arimo",sans-serif}
.icon-x{display:inline-block;vertical-align:middle;margin-right:3px}
.tile{position:absolute;width:55px;height:36px}
</style>
</head>
<body>

<!-- Spread 1: Intro & Services -->
<section class="spread" style="left:8px;top:8px;width:561px;height:397px">
  <div class="abs" role="img" aria-label="Schreibtisch von oben mit Tastatur, Kaffeetasse, Notizblock, Stiften und Blatt einer Pflanze" style="left:281px;top:0;width:280px;height:272px;background:linear-gradient(160deg,#3a4558,#26303f 60%,#1f2836);border-bottom-left-radius:60% 40%"></div>
  <svg class="abs" style="left:281px;top:170px" width="280" height="120" viewBox="0 0 280 120" aria-hidden="true">
    <path d="M0 70 C60 140 130 40 200 80 C240 100 265 60 280 70 L280 120 L0 120 Z" fill="var(--page)"/>
  </svg>

  <div class="abs body bold" style="left:29px;top:30px;width:230px">
    <p>Ordnung. Präsentation. Gestaltung.</p>
    <p>Norvel Plastik steht für individuelle Lösungen für Ordnung und Präsentation.</p>
    <p>Ordnung schaffen wir für Sie mit unseren maßgefertigten Produkten zur strukturierten Ablage im Büro-, Produktions-, sowie Logistikbereich. Mit unseren Produkten gelingt die strukturierte und effiziente Ablage in allen Szenarien.</p>
    <p>Die Präsentation Ihrer Marke ermöglichen wir mit unseren individuell gefertigten und bedruckten Ringbüchern, Ringbuchordnern und Mappen. So gelingt die perfekte Kundenpräsentation verbunden mit einem repräsentativen Auftritt.</p>
    <p>Als Spezialist für Sonderanfertigungen freuen wir uns bei der Gestaltung der Produkte jedem Kunden individuelle Angebote für seinen Anwendungsfall zu erstellen. Dadurch erhalten Sie bei uns nicht bloß einzelne Produkte, sondern ein vollständiges Konzept – Von der Produktgestaltung bis hin zum Layout</p>
    <p style="font-weight:400">Durch unseren langjährigen Erfahrungsschatz können wir jedem Kunden eine individuelle Anpassung unserer Produkte anbieten. Von der technischen Produktgestaltung bis hin zur Layouterstellung erhalten Sie bei uns alles aus einer Hand. Dabei bieten wir gerne auch Kleinauflagen an.</p>
  </div>
  <div class="abs kicker" style="left:29px;top:205px;font-size:13px;color:var(--muted)">SERVICES:</div>
  <div class="abs head-blue" style="left:29px;top:228px;font-size:13px">PRODUKTGESTALTUNG</div>
  <div class="abs body" style="left:29px;top:252px;width:235px;font-size:5.6px">
    <p>Durch unsere langjährige Erfahrung bieten wir Ihnen die vollständige technische Produktgestaltung ihrer Sonderanfertigungen an. In einem individuellen Beratungsgespräch informieren Sie uns über den angedachten Einsatzzweck und Ihre Wünsche an das Produkt und wir skizzieren Ihnen anschließend eine vollständige technische Produktskizze. Dabei prüfen wir wie sich besondere Anforderungen hinsichtlich Materialbeständigkeit oder Funktionalität umsetzen lassen und unterbreiten Ihnen verschiedene Lösungsoptionen und Möglichkeiten.</p>
    <p>Bei komplexeren Vorhaben greifen wir auf ein Netzwerk aus Experten und technischen Zeichnern zurück, um nahezu jedes Vorhaben abbilden zu können.</p>
  </div>
  <div class="abs head-blue" style="left:29px;top:326px;font-size:10px">LAYOUTGESTALTUNG</div>
  <div class="abs body" style="left:29px;top:344px;width:235px;font-size:5.6px">Die optische Gestaltung Ihres Produktes übernehmen wir gerne in Kooperation mit einem weltweiten Netzwerk aus freiberuflichen Grafikern und Designern. Auf Basis Ihrer Vorgaben und unter Berücksichtigung Ihres Corporate Designs können Sie bei uns aus mindestens 30 verschiedenen <span style="font-size:7px">Layout Vorschlägen wählen. Selbst wenn Ihnen keiner der Vorschläge zusagt, berechnen wir Ihnen hierfür keine</span></div>

  <div class="abs" style="left:308px;top:295px;width:86px;height:46px;background:#fff;display:flex;flex-direction:column;align-items:center;justify-content:center;gap:3px">
    <span style="width:12px;height:12px;background:#1f3f8a;display:block"></span>
    <span style="font-size:9px;color:#1f3f8a;font-family:'Source Sans 3',sans-serif">Norvel Plastik</span>
  </div>
  <div class="abs" style="left:302px;top:348px;width:98px;height:14px;border:1px solid var(--blue);border-radius:2px;color:var(--blue);font-family:'Open Sans',sans-serif;font-weight:700;font-size:9px;text-align:center;line-height:12px">NORVEL PLASTIK</div>

  <div class="abs head-blue" style="left:428px;top:276px;font-size:9px">KLEINAUFLAGEN</div>
  <div class="abs body" style="left:428px;top:294px;width:120px;font-size:5.8px;line-height:1.5">Als Produzent von Sonder- und Maßanfertigungen sind wir stolz unseren Kunden bereits ab einer kleinen Auflagenmenge bedienen zu können. Speziell kleineren Unternehmen bieten wir ohne Einschränkungen die Sonderanfertigung kleiner Auflagen all unserer Produktkategorien an.</div>
</section>

<!-- Spread 2: Ordner & Ringbuchordner -->
<section class="spread" style="left:573px;top:8px;width:559px;height:397px">
  <div class="abs head-green" style="left:21px;top:25px;font-size:12px">
    <svg class="icon-x" width="14" height="14" viewBox="0 0 14 14" aria-hidden="true"><path d="M2 2 L12 12 M12 2 L2 12" stroke="#2a2a2a" stroke-width="3"/></svg>ORDNER</div>
  <div class="abs body" style="left:20px;top:45px;font-size:6.5px">Individuell. Bedruckt. Sonderanfertigung. Bedruckt</div>
  <ul class="abs body bullets" style="left:32px;top:59px;width:135px;font-size:6.5px">
    <li>100% individuelles Ordner-Design. Bedruckt nach Ihren Wünschen.</li>
    <li>Vollflächiger Druck möglich. Außen &amp; innen!</li>
    <li>Hochwertige Druckqualität durch modernsten Digitaldruck</li>
    <li>Mehr als 60 Jahre Erfahrung</li>
  </ul>
  <div class="photo" role="img" aria-label="Roter bedruckter Ordner auf Holzboden" style="left:163px;top:63px;width:100px;height:60px;background:radial-gradient(circle at 50% 45%,#d93a3a 0 28%,#9a6a4a 30%,#7b5236)"></div>
  <div class="abs body callout" style="left:20px;top:143px;font-size:6.3px">Mit individuellem Aufdruck werden Aktenordner zum Aushängeschild</div>
  <div class="abs body arimo" style="left:20px;top:165px;width:246px;font-size:6.5px;line-height:1.27">
    <p>Schon in der Bezeichnung kommt der funktionale Zweck von Ordnern zum Ausdruck: Dokumente, Rechnungen, Produktinformationen und mehr lassen sich hier geordnet abheften. So herrscht Ordnung im Büro, Lager oder in der Produktion und dank einer Beschriftung der Ordner sind Unterlagen schnell gefunden. Individuelle Ordner mit einprägsamem Aufdruck übernehmen zudem eine zusätzliche Rolle, die über den funktionalen Aspekt hinausgeht: Sie vermitteln dezent eine Werbebotschaft und tragen als Aushängeschild dazu bei, Ihr Unternehmen und Ihre Marke stilvoll zu präsentieren. Exklusiv und hochwertig, ein Ordner-Design dieser Art bleibt beispielsweise nach einer Produktvorstellung beim Gesprächspartner im Gedächtnis. Bei uns erhalten Sie qualitative und einzigartige Ordner inkl. Druck und Layout Erstellung. Ob Firmenmotto, Logo oder eine Farbgestaltung mit Wiedererkennungseffekt, wir gestalten Ihre Aktenordner exakt nach Ihren Vorgaben. Profitieren Sie von unserer Kreativität und nutzen Sie unsere Kompetenz in puncto moderner Drucktechnik. Vollflächig oder nur teilweise bedruckt, beides ist möglich. Auf Wunsch bedrucken wir individuelle Ordner auch auf der Innenseite.</p>
    <p style="margin-top:8px">Dank hochwertigem Digitaldruck entsteht ein Design mit brillanter Optik. Als Unikat unterstützen die Ordner in bedruckter Ausführung das Alleinstellungsmerkmal Ihres Unternehmens. Auch die Mitarbeiter in den verschiedenen Teams wissen ansprechend gestaltete Ordner zu schätzen. Bei unseren Produkten achten wir ebenso auf eine hohe Qualität: So sind die Ordner stabil und langlebig. Gerne beraten wir Sie hinsichtlich der Gestaltung sowie des Layouts und übermitteln Ihnen ein umfassendes Konzept, das genau auf Ihren Bedarf und Ihre Zielsetzung abgestimmt ist. Machen Sie von der einfachen Möglichkeit einer Anfrage Gebrauch und zögern Sie auch nicht, wenn es sich um eine Kleinauflage handelt.</p>
  </div>

  <div class="abs head-green" style="left:314px;top:54px;font-size:12px">
    <svg class="icon-x" width="16" height="16" viewBox="0 0 14 14" aria-hidden="true"><path d="M2 2 L12 12 M12 2 L2 12" stroke="#3f6fb5" stroke-width="3"/></svg>RINGBUCHORDNER</div>
  <ul class="abs body bullets" style="left:324px;top:77px;width:135px;font-size:5.4px;line-height:1.45">
    <li>Ringbücher aus erstklassigem PVC mit vielen Standardfarben möglich</li>
    <li>100% individueller Druck. Ein- und mehrfarbig</li>
    <li>Von DIN A4 bis DIN A6 sowie diverse Sonderformate</li>
    <li>Stabiler Halt und Stand und Option zur Aufnahme verschiedener Klarsichttaschen (bspw. zur Aufnahme von Visitenkarten etc</li>
  </ul>
  <div class="photo" role="img" aria-label="Pinkfarbener Ringbuchordner" style="left:454px;top:84px;width:97px;height:60px;background:radial-gradient(circle at 52% 50%,#c81e6a 0 22%,#fff 24%)"></div>
  <div class="abs body callout" style="left:314px;top:147px;font-size:6.5px">Hochwertige, individuelle Ringbuchordner</div>
  <div class="abs body" style="left:314px;top:168px;width:240px;font-size:5.8px;line-height:1.48">
    <p>Unsere individuellen Ringbuchordner bestehen aus erstklassigem PVC. Das Format können Sie aus diversen Optionen auswählen, von Standardmaßen wie DIN A4, DIN A5 oder DIN A6 bis zu diversen Sonderformaten ist alles möglich. Sowohl jeder Ordner als auch jedes Ringbuch wird bedruckt - aber nicht nach einheitlichen Vorgaben von uns, sondern zu 100% individuell nach Ihren Vorstellungen. So wird Ihre Marke durch unsere Produkte ideal repräsentiert. Ein PVC-Ringbuchordner von uns ist entweder ein- oder mehrfarbig in zahlreichen Standardfarben erhältlich. Eine Verstärkung mit 2 Millimetern Graupappe bietet jedem individuellen Ringbuch und Ringbuchordner stabilen Halt und Stand und sorgt wie auch das PVC für die hohe Wertigkeit unserer Produkte. Ihre Dokumente können Sie dank der Ringmechanik in verschiedenen Größen und Füllhöhen praktisch in unseren Ordnern abheften. Zudem werden die Nutzungsmöglichkeiten durch weitere Anpassungen entsprechend Ihres Bedarfs erweitert. Zu diesen optionalen Ergänzungen zählen z.B. verschiedene Klarsichttaschen, die unter anderem zur Aufnahme und sicheren Verwahrung von Visitenkarten geeignet sind.</p>
    <p style="margin-top:6px">Unsere Produkte sind kein Mittelmaß, das ohne Anpassungen von jedem Unternehmen genutzt werden kann, sondern einzigartig. Hinter jedem Ringbuch steht ein durchdachtes Konzept, welches auf Ihre Marke zugeschnitten ist. Daher wird Ihre Firma durch unsere Anfertigungen optimal repräsentiert. Die Vorteile unserer Produkte im Überblick: Unsere Ringbücher und Ringbuchordner sind bedruckt - individuell in den unterschiedlichsten Standardfarben und Farbkombinationen. Sie sind aus hochklassigem PVC gefertigt und in verschiedenen Formaten erhältlich. Unsere Anfertigungen haben einen stabilen Stand und Halt und eine Ringmechanik. Zudem ermöglichen wir optionale Extras. Fragen Sie jetzt an, wir freuen uns auf die Zusammenarbeit mit Ihnen!</p>
  </div>
</section>

<!-- Spread 3: Ordnerregister & Hüllen -->
<section class="spread" style="left:8px;top:417px;width:561px;height:398px">
  <div class="abs" style="left:281px;top:0;width:280px;height:398px;background:var(--page-deep)"></div>
  <div class="abs head-green" style="left:37px;top:15px;font-size:11px">ORDNERREGISTER</div>
  <div class="abs body bold" style="left:37px;top:32px;font-size:7.3px">Individuelle Ordnerregister</div>
  <div class="abs body" style="left:39px;top:44px;font-size:6.5px">Für die perfekte Ablage.</div>
  <div class="photo" role="img" aria-label="Geöffneter Ringordner mit weißem Register" style="left:11px;top:59px;width:74px;height:49px;background:radial-gradient(circle at 50% 50%,#f2f0ec 0 40%,#c9b7a3 70%)"></div>
  <ul class="abs body bullets" style="left:94px;top:58px;width:170px;font-size:6.5px;line-height:1.5">
    <li>Individuelle Register aus Karton oder Kunststoff</li>
    <li>Verschiedenste Abläufe oder Formate realisierbar</li>
    <li>100% individueller Druck auf den Tabs sowie auf</li>
    <li>der Registerseite</li>
    <li>Satzweise oder blattweise geliefert</li>
  </ul>
  <div class="abs body callout" style="left:19px;top:116px;font-size:7px">Hochwertige Ordnerregister zur idealen Firmenrepräsentation</div>
  <div class="abs body" style="left:9px;top:133px;width:270px;font-size:6.6px;line-height:1.46">
    <p>Ordnung im Ringbuch – Einfach zu realisieren dank unserer bedruckten Ordnerregister. Diese ermöglichen es Ihnen, Dokumente und andere Schriftstücke übersichtlich zu sortieren. Unsere Ordnerregister im Corporate Design sind in den unterschiedlichsten Formaten erhältlich, sodass sie unabhängig von dessen Format in jedem Ordner verwendet werden können. Neben einer Auswahl an Formaten realisieren wir auch verschiedene Abläufe. Individualität ist dabei von großer Bedeutung, um den Bedürfnissen Ihrer Firma gerecht zu werden: Der Druck ist sowohl auf den Tabs der Ordnerregister als auch auf der Registerseite zu 100% individuell, in welcher Art Ihre Register bedruckt werden - einfarbig oder mehrfarbig - können Sie natürlich selbst wählen. Sie entscheiden ebenfalls - gerne mithilfe unserer professionellen Beratung - ob Ihre Ordnerregister aus Kunststoff oder Karton gefertigt werden und ob die Lieferung satzweise oder blattweise erfolgt. Die satzweise Lieferung macht das Einlegen in die Ringbücher einfacher, während die blattweise Lieferung es erleichtert, Druckinhalte beizulegen. Wählen Sie aus, welche Lieferungsvariante Ihren Verwendungszwecken gerecht wird. Die Realisierung Ihrer Wünsche setzen wir in einem umfangreichen Konzept in unseren Produktionsstätten in Deutschland um. Keine langen Transportwege und keine Massenware von der Stange, sondern individuelle Register, die nach Ihren Wünschen gestaltet und hergestellt sind, sodass sie den Anforderungen Ihrer Marke gerecht werden und diese ideal repräsentieren.</p>
    <p style="margin-top:10px">Die Vorteile unserer individuellen Register auf einen Blick: Das Material - Plastik oder Karton - ist ebenso wie die Abläufe und das Format der Register wählbar. Jedes unserer Register kann bedruckt werden - in den verschiedensten Varianten, ganz nach Ihren Vorstellungen. Die Lieferung erfolgt satz- oder blattweise, auch hier gehen wir selbstverständlich auf Ihre Bedürfnisse ein. Fragen Sie noch heute an und überzeugen Sie sich selbst von unseren individuellen und langlebigen Registern!</p>
  </div>

  <div class="abs head-green" style="left:298px;top:15px;font-size:11px">HÜLLEN &amp; TASCHEN</div>
  <div class="abs body bold" style="left:298px;top:32px;font-size:7.3px">Individuelle Hüllen &amp; Taschen</div>
  <div class="abs body" style="left:301px;top:46px;font-size:6.5px">Damit der Durchblick bleibt.</div>
  <div class="photo" role="img" aria-label="Aufgefächerte schwarze Taschen mit farbigen Kanten" style="left:296px;top:62px;width:74px;height:50px;background:radial-gradient(circle at 50% 50%,#222 0 35%,#3a3a3a 50%,#fff 52%)"></div>
  <ul class="abs body bullets" style="left:377px;top:62px;width:150px;font-size:6.5px;line-height:1.5">
    <li>Individuelle Klarsichthüllen und Taschen in allen Maßen und Stärken</li>
    <li>Optionale Extras wie Ösen oder Schutzkappen möglich</li>
    <li>Kleinauflage möglich</li>
  </ul>
  <div class="abs body callout" style="left:298px;top:116px;font-size:7px">Hochwertige Klarsichthüllen und Taschen individuell abgestimmt</div>
  <div class="abs body" style="left:293px;top:134px;width:263px;font-size:6.6px;line-height:1.46">
    <p>Die individuellen Plastikhüllen und Plastiktaschen sind in den unterschiedlichsten Maßen und Stärken erhältlich. Das Spektrum der Produkte ist breit, da wir auch Sonderanfertigungen unserer individuellen Hüllen aus Qualitätsfolie mit optionalen Extras anbieten: Dazu zählen sowohl Aufdrucke als auch Ösen oder Schutzkappen. Dabei ist es unerheblich, ob Sie eine Kleinauflage oder größere Mengen benötigen, wir bieten Ihnen immer vielfältige Optionen. Die Verwendungsmöglichkeiten der individuellen Plastikhüllen sind sehr umfangreich: Vom Verstauen von Fahrzeugpapieren oder Ausweisen über das Abheften von Dokumenten in gängigen Formaten bis zur sicheren Verwahrung von Dokumenten größerer Maße sind unsere Plastiktaschen und Hüllen vielseitig einsetzbar. Für jeden Verwendungszweck bieten wir Ihnen das ideale Format. In den Hüllen können Dokumente sicher verwahrt werden, in den Ausführungen mit Ösen können die Dokumente dank der individuellen Plastikhüllen auch geschützt abgeheftet werden. Aufgrund ihrer hohen Qualität überzeugen unsere in Deutschland hergestellten Produkte mit Langlebigkeit, sodass Ihre Dokumente optimal geschützt sind und Sie erneute Anschaffungskosten einsparen. Zudem sind die individuellen Hüllen recycelbar. Somit profitieren nicht nur Sie, sondern auch die Umwelt von unseren Produkten.</p>
    <p style="margin-top:6px">Wir liefern Ihnen kein unspezifisches Produkt von der Stange, sondern Plastikhüllen und Taschen, hinter denen ein umfangreiches Konzept steht, welches auf Sie und Ihren Bedarf zugeschnitten ist, sodass Ihre Marke dadurch optimal präsentiert wird. Die Vorteile unserer Produkte zusammengefasst: Unsere Hüllen und Taschen sind in allen Maßen und Stärken erhältlich, es sind Sonderanfertigungen und optionale Ergänzungen, z.B. Ösen oder Schutzkappen möglich und die Auflage ist variabel, auch bei kleineren Mengen bieten wir Individualität. Fragen Sie jetzt an, wir freuen uns auf die Zusammenarbeit mit Ihnen!</p>
  </div>
</section>

<!-- Spread 4: Mappen & Sonderanfertigung -->
<section class="spread" style="left:573px;top:417px;width:562px;height:398px">
  <div class="abs" style="left:267px;top:3px;width:1px;height:392px;background:var(--rule)"></div>
  <div class="abs kicker" style="left:37px;top:16px;font-size:13px;color:var(--muted)">MAPPEN</div>
  <div class="abs kicker" style="left:37px;top:36px;font-size:8.5px;font-weight:400">INDIVIDUELLE MAPPEN</div>
  <div class="abs body" style="left:46px;top:53px;font-size:6.5px">Passend zu Ihren individuellen Wünschen</div>
  <ul class="abs body bullets" style="left:64px;top:68px;font-size:6.5px"><li>Lorem Ipsum sit amet est.</li></ul>
  <div class="abs body" style="left:11px;top:83px;border-left:1.5px solid var(--rule);padding-left:6px;font-size:6.5px;color:var(--green)">Individuelle Mappen – bedarfsgerecht und perfekt für Präsentationen</div>
  <div class="abs body" style="left:19px;top:105px;width:245px;font-size:6.6px;line-height:1.47">Vordergründig lassen sich Mappen zu Ordnungszwecken nutzen. Bei Präsentationen kommt ihnen jedoch eine weitere, ebenso wichtige Aufgabe zu: Versehen mit individuellem Aufdruck, dienen die Hüllen auch dazu, ein Unternehmen darzustellen sowie einen positiven und bleibenden Eindruck bei Geschäftspartnern zu hinterlassen. Ob Meeting oder Kundengespräch, mit Hilfe von professionell gestalteten individuellen Mappen lassen sich Informationen stilvoll mit einer Markenbotschaft oder einer Firmenphilosophie verknüpfen. Unsere Mappen bedruckt entsprechen in hohem Maße allen diesen Anforderungen. Das Firmenlogo verbunden mit einer Werbebotschaft, die charakteristischen Farben Ihres Unternehmens, eine Gesamtgestaltung auf hohem Niveau, wir erstellen Produkte genau nach Ihren Vorstellungen und wenden dabei hochwertige Druckverfahren an. Nutzen Sie die Möglichkeit einer Anfrage oder rufen Sie uns an: Basierend auf einem umfassenden Konzept fertigen wir Ihre individuellen Mappen. Nicht nur bei der spezifischen Gestaltung, sondern auch hinsichtlich Größe, Farbe, Material und Beschichtung stellen wir uns auf Ihre Wünsche ein. Dank diverser Formate und Volumen der Taschen finden Unterlagen in unterschiedlicher Größe und Zahl den nötigen Platz. Unsere Mappen sind aus PVC in verschiedener Stärke gefertigt und mit der jeweils geeigneten Beschichtung versehen. So sind Dokumente oder Informationsmaterial vor Beschädigungen geschützt und lassen sich problemlos zu den jeweiligen Arbeitsorten oder auch zu Verkaufsmessen transportieren. Die bedruckten Mappen eignen sich ebenso für eine gut durchdachte Ablage, denn eine optimale Archivierung spart Zeit bei den Arbeitsabläufe. Sie sind in zahlreichen Farben erhältlich und lassen sich mit zusätzlichen Merkmalen wie Ösen ausstatten. Zudem zeichnen sie sich durch eine hohe Qualität aus und sind langlebig. Ob beispielsweise Werkstattmappen, Pflegemappen, Konferenz- oder Werbehüllen, unsere Produkte erfüllen optimal ihren Ordnungszweck und strahlen durch ihr Design die gewünschte Seriosität aus.</div>

  <div class="abs kicker" style="left:320px;top:17px;width:171px;height:23px;border:1px solid var(--ink);font-size:13px;font-weight:400;text-align:center;line-height:21px">SONDERANFERTIGUNGE</div>
  <div class="abs body bold" style="left:360px;top:43px;font-size:8.3px">Sonderanfertigungen</div>
  <div class="abs body" style="left:342px;top:58px;font-size:6.5px">✥&nbsp; Wir machen Persönliches möglich</div>
  <div class="abs body" style="left:314px;top:79px;width:200px;font-size:6.8px;line-height:1.3">Unsere Sonderabfertigungen zeichnen sich durch einen hohen technischen Standard, viele verschiedene Größen und gute Umsetzbarkeit aus.</div>
  <div class="abs" style="left:352px;top:121px;width:110px;height:25px;background:var(--slate);border-radius:2px;clip-path:polygon(6% 0,100% 0,100% 88%,95% 100%,0 100%,0 12%);font-size:8.3px;text-align:center;line-height:25px">Produkt-Headline</div>
  <div class="abs body bold" style="left:291px;top:152px;width:238px;height:38px;border:1px solid #3a6a2a;font-size:5.2px;text-align:center;padding-top:3px;line-height:1.45">Sonderanfertigungen wie Tischtennis Umrandungen, Fahrzeugscheinmappen oder Werkstattmappen für Autowerkstätten (um nur einige wenige Bereiche zu nennen) sind für uns Tagesgeschäft – bitte fragen Sie an- ich denke wir können Ihnen aus unserer Erfahrung hier fachgerechte Lösungen anbieten.</div>

  <svg class="abs" style="left:291px;top:197px" width="241" height="178" viewBox="0 0 241 178" aria-hidden="true">
    <path d="M1 1 H240 V150 C200 130 180 170 130 176 C80 180 40 160 1 170 Z" fill="none" stroke="var(--gold)" stroke-width="1.2"/>
  </svg>
  <div class="tile" role="img" aria-label="Blaue Mappe auf Holzboden" style="left:296px;top:203px;background:linear-gradient(135deg,#1c4fb8 50%,#7d6a58 50%)"></div>
  <div class="tile" role="img" aria-label="Transparente Hülle auf Holzboden" style="left:355px;top:203px;background:linear-gradient(135deg,#8f8a86,#6f6558)"></div>
  <div class="tile" role="img" aria-label="Weißer Ordner auf Holzboden" style="left:413px;top:203px;background:linear-gradient(90deg,#7a6555 40%,#eee 40% 60%,#7a6555 60%)"></div>
  <div class="tile" role="img" aria-label="Roter Ordner auf Holzboden" style="left:472px;top:203px;background:linear-gradient(90deg,#7a6555 25%,#d42a2a 25% 75%,#7a6555 75%)"></div>
  <div class="tile" role="img" aria-label="Rote Mappe auf Holzboden" style="left:296px;top:244px;background:linear-gradient(135deg,#7a6555 30%,#d42a2a 30% 70%,#7a6555 70%)"></div>
  <div class="tile" role="img" aria-label="Rote Mappe aufgeklappt" style="left:355px;top:244px;background:linear-gradient(150deg,#7a6555 30%,#e03434 30% 75%,#7a6555 75%)"></div>
  <div class="tile" role="img" aria-label="Weißer Ordner mit rotem Rücken" style="left:413px;top:244px;background:linear-gradient(90deg,#7a6555 35%,#f2f2f2 35% 65%,#7a6555 65%)"></div>
  <div class="tile" role="img" aria-label="Geöffneter Ringordner mit grünem Rand" style="left:472px;top:244px;background:linear-gradient(135deg,#eeeeea,#c8c8c2);border:1px solid #1c7a3a"></div>
  <div class="tile" role="img" aria-label="Rote Mappe flach liegend" style="left:296px;top:285px;background:linear-gradient(160deg,#d62a2a 60%,#7a6555 60%)"></div>
  <div class="tile" role="img" aria-label="Graue Hülle flach liegend" style="left:355px;top:285px;background:linear-gradient(135deg,#4a4a50,#6f6558)"></div>
  <div class="tile" role="img" aria-label="Weißer Ringordner geöffnet" style="left:413px;top:285px;background:linear-gradient(135deg,#f2f2f0,#d2d0cc)"></div>
  <div class="tile" role="img" aria-label="Blaue Mappe mit Sichtfenster" style="left:472px;top:285px;background:linear-gradient(135deg,#1f6fd0 60%,#7a6555 60%)"></div>
  <div class="tile" role="img" aria-label="Transparente Hülle auf Holzboden" style="left:299px;top:327px;background:linear-gradient(135deg,#9a96a0,#6f6558)"></div>
</section>

</body>
</html>
```